Essential oil label for bottles

Looking to modify our current logo and label design. It looks too simple. I will attach images of our competitors to use as examples. Our company name is Velnora. We have 2 different bottles. Clear and amber color. Going forward, we will be using only the amber bottle. The other 2 images are the biggest sellers brands. We want to make some adjustments to ours.

Target Market(s)

Brindex sales

Industry/Entity Type

Essential oil, perfume

Colors

Designer to choose only greyscale colors for use in the design.

Requirements
Nice to have
• A slight change to fonts and logo design. Maybe change the font and design of the word "Velnora" in our logo. Maybe add something to the label to make it stand out more but still keeping it clean and modern
Should not have
• No colors, besides, black, grays, whites, and off white.

```html
<!DOCTYPE html>
<html lang="en">
<head>
<meta charset="utf-8">
<title>Velnora – Essential Oil Label</title>
<link href="https://fonts.googleapis.com/css2?family=Montserrat:wght@300;400;500;600;700&family=Inter:wght@400;600&display=swap" rel="stylesheet">
<style>
  :root {
    --paper: #ffffff;
    --panel: #f9f9f9;
    --ink: #222222;
    --ink-soft: #444444;
    --muted: #8a8a8a;
    --rule: #bdbdbd;
    --dark-label: #222222;
    --on-dark: #f2f2f2;
    --on-dark-muted: #9a9a9a;
    --display: "Montserrat", Arial, sans-serif;
    --body: "Inter", Arial, sans-serif;
  }
  * { box-sizing: border-box; margin: 0; padding: 0; }
  html, body { width: 1200px; height: 3125px; overflow: hidden; background: var(--paper); }
  .board { position: relative; width: 1200px; height: 3125px; background: var(--paper); color: var(--ink); font-family: var(--display); }

  /* brand name lockup */
  .brand { display: flex; align-items: center; gap: 10px; font-family: var(--display); font-weight: 500; letter-spacing: 0.28em; color: inherit; white-space: nowrap; }
  .brand__dot { width: 0.9em; height: 0.9em; border-radius: 50%; border: 2px solid currentColor; flex: none; }

  /* intro */
  .intro-mark { position: absolute; left: 184px; top: 152px; width: 237px; height: 237px; border: 1px solid #555; border-radius: 6px; display: flex; align-items: center; justify-content: center; }
  .intro-mark .brand { font-size: 26px; font-weight: 600; }
  .intro-lockup { position: absolute; left: 673px; top: 194px; }
  .intro-lockup .brand { font-size: 33px; gap: 18px; }
  .intro-lockup .brand__dot { border-width: 3px; }
  .intro-caption { position: absolute; left: 600px; top: 318px; width: 430px; text-align: center; font-family: var(--display); font-weight: 300; font-size: 14px; line-height: 18px; color: var(--muted); }

  /* photo areas */
  .photo { position: absolute; }
  .photo--dropper { left: 0; top: 550px; width: 600px; height: 884px; background: linear-gradient(180deg, #dcdce1 0%, #d6d6db 65%, #8c8377 78%, #a49b8f 88%, #d9d9dd 100%); }
  .photo--flatlay { left: 0; top: 2548px; width: 1200px; height: 577px; background: linear-gradient(120deg, #9a9a9a 0%, #e4e4e4 22%, #ececec 55%, #d8d4c8 80%, #bdbdbd 100%); }

  .showcase { position: absolute; left: 600px; top: 550px; width: 600px; height: 884px; background: var(--panel); }

  /* label surfaces */
  .label { position: absolute; background: var(--panel); border: 1px solid #555; }
  .label--single { left: 716px; top: 732px; width: 366px; height: 521px; }
  .label--wrap { left: 125px; top: 1470px; width: 916px; height: 520px; }
  .label--dark { left: 129px; top: 1990px; width: 910px; height: 521px; background: var(--dark-label); border: none; color: var(--on-dark); }

  .front__brand { position: absolute; left: 61px; top: 64px; }
  .front__brand .brand { font-size: 19px; }
  .front__title { position: absolute; left: 61px; top: 240px; font-size: 41px; line-height: 1; font-weight: 300; letter-spacing: 0.02em; white-space: nowrap; }
  .front__title b { font-weight: 700; }
  .front__volume { position: absolute; left: 167px; top: 287px; display: flex; align-items: center; gap: 8px; font-size: 14px; font-weight: 500; letter-spacing: 0.04em; }
  .front__volume::before { content: ""; width: 51px; height: 1px; background: currentColor; opacity: .5; }
  .front__kind { position: absolute; left: 61px; top: 412px; font-size: 12px; font-weight: 700; letter-spacing: 0.01em; }
  .front__kind-rule { position: absolute; left: 61px; top: 434px; width: 30px; height: 1px; background: var(--rule); }
  .front__notes { position: absolute; left: 61px; top: 444px; display: flex; font-size: 12px; font-weight: 400; letter-spacing: 0.02em; }
  .front__notes span + span { border-left: 1px solid var(--rule); margin-left: 8px; padding-left: 8px; }

  .spine { position: absolute; left: 416px; top: 160px; height: 188px; writing-mode: vertical-rl; transform: rotate(180deg); display: flex; align-items: center; gap: 8px; white-space: nowrap; }
  .spine__title { font-size: 22px; font-weight: 300; letter-spacing: 0.02em; }
  .spine__title b { font-weight: 700; }
  .spine__rule { width: 1px; height: 22px; background: currentColor; opacity: .5; }
  .spine__volume { font-size: 7px; font-weight: 600; letter-spacing: 0.05em; }

  .back__divider { position: absolute; left: 558px; top: 65px; width: 1px; height: 403px; background: var(--rule); }
  .back__copy { position: absolute; left: 578px; top: 68px; width: 290px; font-family: var(--body); font-size: 13px; line-height: 18.5px; letter-spacing: -0.01em; color: var(--ink-soft); }
  .back__copy p + p { margin-top: 18.5px; }
  .back__copy strong { font-weight: 600; color: var(--ink); }
  .label--dark .back__copy, .label--dark .back__copy strong { color: var(--on-dark); }
  .back__rule { position: absolute; left: 578px; top: 377px; width: 211px; height: 1px; background: var(--rule); }
  .label--dark .back__rule, .label--dark .back__divider { background: #555; }
  .back__brand { position: absolute; left: 578px; top: 428px; }
  .back__brand .brand { font-size: 12px; gap: 7px; }
  .back__brand .brand__dot { border-width: 1.5px; }
  .back__tagline { position: absolute; left: 733px; top: 418px; font-family: var(--body); font-size: 13px; line-height: 18.5px; color: var(--muted); }
  .label--dark .back__tagline { color: var(--on-dark-muted); }
</style>
</head>
<body>
<main class="board">

  <section class="intro">
    <div class="intro-mark"><div class="brand"><span class="brand__dot"></span>VELNORA</div></div>
    <div class="intro-lockup"><div class="brand"><span class="brand__dot"></span>VELNORA</div></div>
    <p class="intro-caption">To give the logo some personality, I added a curve that flows with the essence of the fragrance.</p>
  </section>

  <div class="photo photo--dropper" role="img" aria-label="Amber dropper bottle with the White Tea label standing on a stone slab, golden oil dripping from the pipette, light grey backdrop"></div>

  <section class="showcase">
  </section>

  <article class="label label--single">
    <div class="front__brand"><div class="brand"><span class="brand__dot"></span>VELNORA</div></div>
    <h2 class="front__title">WHITE <b>TEA</b></h2>
    <div class="front__volume">200 ML</div>
    <div class="front__kind">FRAGRANCE OIL</div>
    <div class="front__kind-rule"></div>
    <div class="front__notes"><span>WHITE TEA</span><span>ORANGE</span><span>PALO SANTO</span></div>
  </article>

  <article class="label label--wrap">
    <div class="front__brand"><div class="brand"><span class="brand__dot"></span>VELNORA</div></div>
    <h2 class="front__title">WHITE <b>TEA</b></h2>
    <div class="front__volume">200 ML</div>
    <div class="front__kind">FRAGRANCE OIL</div>
    <div class="front__kind-rule"></div>
    <div class="front__notes"><span>WHITE TEA</span><span>ORANGE</span><span>PALO SANTO</span></div>
    <div class="spine"><span class="spine__title">WHITE <b>TEA</b></span><span class="spine__rule"></span><span class="spine__volume">200 ML</span></div>
    <div class="back__divider"></div>
    <div class="back__copy">
      <p><strong>DIRECTIONS:</strong> Take one or two capsules after meals. Do not exceed three capsules per day Take during real-time cravings or before drinking situations for additional craving support. Store in a cool dry place, tightly closed. Keep away from children.</p>
      <p><strong>WARNING:</strong> Not to be used by children under 18 ears, women who are pregnant, may become pregnant, breastfeeding, people taking antidepressant drugs or sedatives. If you are under a physician's care or taking any medications, or being treated for heart disease or diabetes, consult your health care: professional before taking this product.</p>
    </div>
    <div class="back__rule"></div>
    <div class="back__brand"><div class="brand"><span class="brand__dot"></span>VELNORA</div></div>
    <p class="back__tagline">Best essential oils<br>from Velnora</p>
  </article>

  <article class="label label--dark">
    <div class="front__brand"><div class="brand"><span class="brand__dot"></span>VELNORA</div></div>
    <h2 class="front__title">WHITE <b>TEA</b></h2>
    <div class="front__volume">200 ML</div>
    <div class="front__kind">FRAGRANCE OIL</div>
    <div class="front__kind-rule"></div>
    <div class="front__notes"><span>WHITE TEA</span><span>ORANGE</span><span>PALO SANTO</span></div>
    <div class="spine"><span class="spine__title">WHITE <b>TEA</b></span><span class="spine__rule"></span><span class="spine__volume">200 ML</span></div>
    <div class="back__divider"></div>
    <div class="back__copy">
      <p><strong>DIRECTIONS:</strong> Take one or two capsules after meals. Do not exceed three capsules per day Take during real-time cravings or before drinking situations for additional craving support. Store in a cool dry place, tightly closed. Keep away from children.</p>
      <p><strong>WARNING:</strong> Not to be used by children under 18 ears, women who are pregnant, may become pregnant, breastfeeding, people taking antidepressant drugs or sedatives. If you are under a physician's care or taking any medications, or being treated for heart disease or diabetes, consult your health care: professional before taking this product.</p>
    </div>
    <div class="back__rule"></div>
    <div class="back__brand"><div class="brand"><span class="brand__dot"></span>VELNORA</div></div>
    <p class="back__tagline">Best essential oils<br>from Velnora</p>
  </article>

  <div class="photo photo--flatlay" role="img" aria-label="Amber bottle with the White Tea label lying diagonally on a pale stone surface with soft window shadows"></div>

</main>
</body>
</html>
```